New solo practice law firm is looking for an elegant, professional, and interactive web design

I need a web design and developer for a new small law firm in Sacramento, California called Dorian Kessel Law, A Professional Corporation. I am a trial lawyer who represents average people facing difficult litigation disputes, including criminal defense as a former prosecutor and civil litigation as a civil litigator. Criminal defense includes domestic violence, battery, assault, drug possession, theft, DUI, etc. Civil litigation includes business disputes, property disputes, employment disputes, family law disputes, and immigration issues. I would like to see web designs that incorporate my logo and use the logo's navy blue and gold colors. I have uploaded the files of my logo to this brief. Please only use the navy blue and gold version. Overall, I want the design to look firm, professional, and elegant.

I plan on having the following pages on my website: (1) Home, (2) Dorian Kessel, (3) Practice Areas, (4) Insights, (5) Contact. I've hand drawn a preliminary sketch concept of what I envision the home page's layout to look like (attached with a text version). I would like your design to keep a similar layout for the homepage and incorporate my logo's colors within it but I am open to creative layout alternatives/ideas. I would like the other pages to have a similar look and feel as the home page. Some of the areas currently in my sketch do not have the full text. You can insert other text for now and I will provide the winner the full text.

In terms of the pictures on the website, I enjoy images of courthouses, columns (example attached but I cannot use this one), and, if possible, images from Sacramento, CA in my background (headshot attached). A plus would be live images that move and also sections of the webpage moving in the viewers view as they scroll down on the page. Also, it would be great to have my logo act as the tab for the website. I can provide other versions of the logo if needed.

I look forward to seeing your Wordpress designs!

People needing legal representation.

Law

Coded - Design and coding required

5+ page

Serif

• Incorporate my logo and my logo's colors.
• Live pictures and images appearing as viewers scroll on page.

```html
<!DOCTYPE html>
<html lang="en">
<head>
<meta charset="utf-8">
<title>Dorian Kessel Law — Home</title>
<link rel="stylesheet" href="https://fonts.googleapis.com/css2?family=Merriweather:ital,wght@0,400;1,400&family=Montserrat:wght@400;500;600&display=swap">
<style>
  :root {
    --navy: #1c2f55;
    --navy-deep: #0e1a34;
    --navy-mid: #2d4675;
    --sky: #7f93b8;
    --gold: #b0925a;
    --ink: #1e2230;
    --paper: #ffffff;
  }
  * { box-sizing: border-box; margin: 0; padding: 0; }
  html, body { width: 1200px; height: 675px; overflow: hidden; background: var(--paper); }
  body { position: relative; font-family: "Montserrat", sans-serif; color: var(--ink); }

  .site-header { position: absolute; left: 0; top: 0; width: 1200px; height: 56px; }
  .brand { position: absolute; left: 98px; top: 12px; display: flex; align-items: center; gap: 8px; }
  .brand-mark { width: 30px; height: 30px; border: 1.5px solid var(--gold); }
  .brand-name { font-family: "Merriweather", serif; font-size: 8px; letter-spacing: 1.2px; color: var(--gold); text-transform: uppercase; line-height: 1.5; }
  .brand-name small { display: block; font-size: 5.5px; letter-spacing: 0.8px; }

  .main-nav { position: absolute; left: 456px; top: 0; height: 56px; display: flex; gap: 19px; align-items: center; }
  .main-nav a { font-size: 9.5px; font-weight: 500; color: var(--ink); text-decoration: none; position: relative; }
  .main-nav a.is-active { color: var(--gold); }
  .main-nav a.is-active::after { content: ""; position: absolute; left: 50%; top: 15px; width: 3px; height: 3px; margin-left: -1.5px; border-radius: 50%; background: var(--gold); }

  .header-phone { position: absolute; left: 1018px; top: 20px; display: flex; align-items: center; gap: 6px; font-size: 9.5px; font-weight: 500; }

  .hero { position: absolute; left: 0; top: 56px; width: 1107px; height: 560px; border-top-right-radius: 10px; overflow: hidden; }
  .hero-photo { position: absolute; inset: 0;
    background:
      radial-gradient(ellipse 55% 40% at 70% 8%, rgba(170,185,212,.75) 0%, transparent 70%),
      radial-gradient(ellipse 60% 70% at 72% 55%, rgba(92,118,165,.55) 0%, transparent 70%),
      linear-gradient(180deg, #4a6290 0%, var(--navy-mid) 35%, var(--navy) 65%, var(--navy-deep) 100%); }
  .hero-shade { position: absolute; inset: 0; background: linear-gradient(90deg, rgba(14,26,52,.55) 0%, rgba(14,26,52,0) 55%); }
  .hero-copy { position: absolute; left: 138px; top: 194px; color: #fff; }
  .hero-eyebrow { font-size: 8.5px; font-weight: 500; letter-spacing: 0.4px; margin-bottom: 10px; }
  .hero-title { font-family: "Merriweather", serif; font-weight: 400; font-size: 28px; line-height: 1.25; }
  .hero-accent { font-family: "Merriweather", serif; font-style: italic; font-size: 28px; color: var(--gold); margin-top: 4px; }
  .hero-cta { margin-top: 22px; display: inline-flex; align-items: center; gap: 8px; height: 32px; padding: 0 14px 0 10px; border: 1.5px solid #fff; border-radius: 16px; font-size: 11px; letter-spacing: 0.3px; color: #fff; }

  .slide-index { position: absolute; left: 0; top: 256px; color: #fff; font-size: 14px; }
  .slide-index li { list-style: none; height: 27px; padding-left: 58px; position: relative; }
  .slide-index li.is-current { color: var(--gold); padding-left: 54px; }
  .slide-index li.is-current::before { content: ""; position: absolute; left: 0; top: 9px; width: 40px; height: 1.5px; background: var(--gold); }

  .slide-arrows { position: absolute; left: 752px; top: 540px; display: flex; gap: 22px; }

  .watch-video { position: absolute; right: 0; bottom: 0; width: 118px; height: 48px;
    background: linear-gradient(120deg, #4a3a26, #7a5d35 60%, #3a2d1d); display: flex; align-items: center; gap: 7px; padding-left: 10px; color: #fff; font-size: 9px; white-space: nowrap; }
  .play-btn { width: 24px; height: 24px; flex: none; border-radius: 50%; background: #fff; display: flex; align-items: center; justify-content: center; }

  .social-list { position: absolute; left: 1146px; top: 312px; list-style: none; }
  .social-list li { width: 12px; height: 12px; margin-bottom: 18px; border: 1.5px solid var(--ink); border-radius: 3px; }

  .section-label { position: absolute; left: 243px; top: 636px; display: flex; align-items: center; gap: 40px; font-size: 7px; letter-spacing: 2.4px; color: var(--gold); text-transform: uppercase; }
  .section-label::before { content: ""; width: 4px; height: 4px; border-radius: 50%; background: var(--gold); }
</style>
</head>
<body>
  <header class="site-header">
    <div class="brand">
      <span class="brand-mark"></span>
      <span class="brand-name">Dorian Kessel Law<small>A Professional Corporation</small></span>
    </div>
    <nav class="main-nav">
      <a href="#" class="is-active">Home</a>
      <a href="#">Dorian Kessel</a>
      <a href="#">Practice Areas</a>
      <a href="#">Insights</a>
      <a href="#">Contact</a>
    </nav>
    <div class="header-phone">
      <svg width="12" height="12" viewBox="0 0 24 24" fill="none" stroke="#b0925a" stroke-width="2"><path d="M22 16.9v3a2 2 0 0 1-2.2 2 19.8 19.8 0 0 1-8.6-3.1 19.5 19.5 0 0 1-6-6A19.8 19.8 0 0 1 2.1 4.2 2 2 0 0 1 4.1 2h3a2 2 0 0 1 2 1.7c.1.9.4 1.8.7 2.7a2 2 0 0 1-.5 2.1L8 9.8a16 16 0 0 0 6 6l1.3-1.3a2 2 0 0 1 2.1-.4c.9.3 1.8.6 2.7.7a2 2 0 0 1 1.7 2z"/></svg>
      (916) 555-0142
    </div>
  </header>

  <section class="hero">
    <div class="hero-photo" role="img" aria-label="Low-angle photo of a domed state capitol courthouse with tall columns under a cloudy sky, tinted navy blue"></div>
    <div class="hero-shade"></div>

    <ol class="slide-index">
      <li>01</li>
      <li class="is-current">02</li>
      <li>03</li>
      <li>04</li>
      <li>05</li>
    </ol>

    <div class="hero-copy">
      <p class="hero-eyebrow">LEGAL COUNSELING</p>
      <h1 class="hero-title">If you have any<br>legal problem in your life...</h1>
      <p class="hero-accent">I am available</p>
      <span class="hero-cta">
        <svg width="14" height="14" viewBox="0 0 24 24" fill="#fff"><path d="M3 4h12a2 2 0 0 1 2 2v6a2 2 0 0 1-2 2H8l-4 3v-3H3a2 2 0 0 1-2-2V6a2 2 0 0 1 2-2z"/><path d="M19 8h2a2 2 0 0 1 2 2v6a2 2 0 0 1-2 2h-1v3l-4-3h-5a2 2 0 0 1-2-2v-1h6a3 3 0 0 0 3-3z" opacity=".8"/></svg>
        GET CONSULTATION
      </span>
    </div>

    <div class="slide-arrows">
      <svg width="46" height="10" viewBox="0 0 46 10" fill="none" stroke="#fff" stroke-width="1.5"><path d="M45 5H2M6 1L2 5l4 4"/></svg>
      <svg width="46" height="10" viewBox="0 0 46 10" fill="none" stroke="#fff" stroke-width="1.5"><path d="M1 5h43M40 1l4 4-4 4"/></svg>
    </div>

    <div class="watch-video">
      <span class="play-btn"><svg width="8" height="8" viewBox="0 0 10 10"><path d="M2 1l7 4-7 4z" fill="#b0925a"/></svg></span>
      WATCH VIDEO
    </div>
  </section>

  <ul class="social-list" aria-label="Social links">
    <li aria-label="Social profile 1"></li>
    <li aria-label="Social profile 2"></li>
    <li aria-label="Social profile 3"></li>
    <li aria-label="Social profile 4"></li>
  </ul>

  <p class="section-label">Who I am</p>
</body>
</html>
```